Business Card 85x40mm - Freelance audio mixing / live event operator

I am a freelance audio operator working in live events. Mostly corporate events mixing sound for a range of entertainment, awards nights and functions. I need a new card to give to perspective clients.

The final design will convey bold professionalism with a general dark vibe. Looking for dark-ish background with some smatterings of colour added.

I have attatched my old BC for an idea of what I have liked in the past. Id like a more modern updated design (that circular design on the back is not my logo it is just a picture I found that resembled sound} . For an added element possibly a mixture of some playful colours in a way that resembles an audio wave form or sound.

I have attached a photo called "audio software" with some colourful squiggly lines; maybe incorporate elements of that into into design
Updates

Added extra $ to project Damn Pixel hives fees are unreasonable

Target Market(s)

Mostly corporate clients

Industry/Entity Type

Events

Contact Information for Business Card

Corwin Pellath
Sound | FOH | Monitors | Systems | Corporate

Digital Audio Mixing Specialist, Live Event Technical Professional,

corwinpellath@mailvexo.net, +61 402 918 357

Colors
ec1f27
ffc214
9bcb3c
6b449b

Requirements
Must have
• Dark theme
• 85x40mm dimensions
Nice to have
• some sort of imagery or design to reflect audio/sound

```html
<!DOCTYPE html>
<html lang="en">
<head>
<meta charset="utf-8">
<title>Corwin Pellath – Business Card</title>
<link rel="stylesheet" href="https://fonts.googleapis.com/css2?family=Arvo:wght@400;700&family=Open+Sans:wght@400;600&display=swap">
<style>
  :root {
    --backdrop: #d9d9d9;
    --card: #050505;
    --card-band: #161616;
    --red: #ec1f27;
    --yellow: #ffc214;
    --green: #9bcb3c;
    --purple: #6b449b;
    --cyan: #2fd6e8;
    --blue: #1e7ff0;
    --orange: #f57a12;
    --text: #f2f2f2;
    --muted: #e6e6e6;
  }
  * { box-sizing: border-box; margin: 0; padding: 0; }
  html, body {
    width: 1200px;
    height: 900px;
    overflow: hidden;
  }
  body {
    background: var(--backdrop);
    position: relative;
    font-family: "Open Sans", Arial, sans-serif;
  }
  .card {
    position: absolute;
    left: 320px;
    width: 560px;
    height: 264px;
    border-radius: 28px;
    background: var(--card);
    overflow: hidden;
  }
  .card--front { top: 140px; }
  .card--back { top: 490px; }

  /* Front */
  .front-identity {
    position: absolute;
    left: 42px;
    top: 62px;
    display: flex;
    align-items: center;
    gap: 12px;
  }
  .front-identity__mark {
    width: 22px;
    height: 22px;
    background: var(--red);
  }
  .front-identity__name {
    font-family: "Arvo", Georgia, serif;
    font-weight: 700;
    font-size: 26px;
    color: var(--yellow);
    letter-spacing: 0.5px;
  }
  .front-identity__rule {
    position: absolute;
    left: 42px;
    top: 104px;
    width: 240px;
    height: 2px;
    background: var(--red);
  }
  .soundwave {
    position: absolute;
    left: 0;
    right: 0;
    top: 128px;
    height: 70px;
    border-radius: 35px;
    background: linear-gradient(90deg, var(--orange) 0%, var(--yellow) 22%, var(--green) 48%, var(--cyan) 78%, var(--blue) 100%);
    opacity: 0.85;
    filter: blur(3px);
  }

  /* Back */
  .back-band {
    position: absolute;
    left: 0;
    right: 0;
    bottom: 0;
    height: 120px;
    background: var(--card-band);
  }
  .back-identity {
    position: absolute;
    left: 36px;
    top: 40px;
    display: flex;
    align-items: center;
    gap: 12px;
  }
  .back-identity__mark {
    width: 20px;
    height: 20px;
    background: var(--red);
  }
  .back-identity__name {
    font-weight: 600;
    font-size: 22px;
    color: var(--text);
  }
  .services {
    position: absolute;
    right: 30px;
    top: 112px;
    text-align: right;
    font-size: 15px;
    line-height: 19px;
    color: var(--muted);
    letter-spacing: 0.3px;
  }
  .details {
    position: absolute;
    left: 36px;
    bottom: 24px;
    color: var(--text);
    font-size: 14px;
    line-height: 18px;
  }
  .details__role { margin-bottom: 6px; }
  .details__line {
    display: flex;
    align-items: center;
    gap: 7px;
    font-size: 15px;
    line-height: 20px;
  }
  .details__icon { width: 14px; height: 14px; flex: none; }
</style>
</head>
<body>

  <section class="card card--front">
    <div class="front-identity">
      <span class="front-identity__mark"></span>
      <span class="front-identity__name">Corwin Pellath</span>
    </div>
    <div class="front-identity__rule"></div>
    <div class="soundwave" role="img" aria-label="Colourful glowing audio waveform of many fine lines, orange through yellow and green to cyan and blue"></div>
  </section>

  <section class="card card--back">
    <div class="back-band"></div>
    <div class="back-identity">
      <span class="back-identity__mark"></span>
      <span class="back-identity__name">Corwin Pellath</span>
    </div>
    <p class="services">Sound | FOH | Monitors<br>Systems | Corporate</p>
    <div class="details">
      <p class="details__role">Digital Audio Mixing Specialist,<br>Live Event Technical Professional</p>
      <p class="details__line">
        <svg class="details__icon" viewBox="0 0 16 16" aria-hidden="true">
          <path fill="#9bcb3c" d="M3.5 1.5l2.5 2.8-1.3 1.7c.9 1.9 2.4 3.4 4.3 4.3l1.7-1.3 2.8 2.5-1.4 2.5C7 13.6 2.4 9 1 3z"/>
        </svg>
        +61 402 918 357
      </p>
      <p class="details__line">
        <svg class="details__icon" viewBox="0 0 16 16" aria-hidden="true">
          <rect x="1" y="3" width="14" height="10" fill="#9bcb3c"/>
          <path d="M1.5 3.5L8 9l6.5-5.5" fill="none" stroke="#050505" stroke-width="1.4"/>
        </svg>
        corwinpellath@mailvexo.net
      </p>
    </div>
  </section>

</body>
</html>
```